Tallowmoor Letterheads Design

Hello, we have just upgraded this project for a guaranteed payment.

We are currently going through a re-branding exercise internally. Our logo is attached as a PDF file.

We are happy with our logo but would like to investigate how we can best apply the logo to our letterheads and compliment slips.

We are a quality printing company in England. Despite our name we are very professional and offer a personal service.

Our new website is under construction and here is a link to show you how it looks: http://brackenpress.v4ntor.co.uk

The style must be professional and steer away from "tacky" otherwise it makes our company look very low budget and just a bit silly.

We would like to see elements of creativity though, so please, nothing too boring.

I have attached our new logo, there is an option for use on white or black.

Cheers
Tallowmoor Team

Reason: We have increased the deadline due to an internal delay to things, we now have more time before we need anything to be printed.

Industry/Entity Type

Construction

Requirements
Must have
• IMPORTANT! Please do not tweak or change our logo in any way. A few designs show vast changes in the logo, this is not what we require. Please do not change the logo in any way. Thanks
Nice to have
• Classy but approachable. Elements of "quirky" would be nice to see.
Should not have
• A Tacky feel

```html
<!DOCTYPE html>
<html lang="en">
<head>
<meta charset="utf-8">
<title>Tallowmoor Letterhead</title>
<link rel="stylesheet" href="https://fonts.googleapis.com/css2?family=Montserrat:wght@500;700&display=swap">
<style>
  :root {
    --ink-band: #1b1e21;
    --paper: #ffffff;
    --brand-pink: #e61f7e;
    --soft-pink: #f49ac1;
    --mascot-grey: #939598;
    --edge-grey: #c9cacc;
  }
  * { margin: 0; padding: 0; box-sizing: border-box; }
  html, body { width: 927px; height: 1200px; overflow: hidden; background: var(--paper); }
  .letterhead {
    position: relative;
    width: 927px;
    height: 1200px;
    background: var(--paper);
    border-left: 2px solid var(--edge-grey);
    font-family: "Montserrat", Arial, sans-serif;
    overflow: hidden;
  }
  .masthead {
    position: absolute;
    inset: 0 0 auto 0;
    height: 182px;
    background: var(--ink-band);
  }
  .brand {
    position: absolute;
    right: 36px;
    top: 36px;
    display: flex;
    flex-direction: column;
    align-items: center;
    gap: 10px;
  }
  .brand-dot {
    width: 50px;
    height: 50px;
    border-radius: 50%;
    background: var(--brand-pink);
  }
  .brand-name {
    color: var(--paper);
    font-weight: 700;
    font-size: 31px;
    letter-spacing: -0.5px;
    line-height: 1;
  }
  .mascot-art {
    position: absolute;
    left: 0;
    bottom: 0;
    width: 470px;
    height: 500px;
    border-top-right-radius: 240px 260px;
    background: linear-gradient(160deg, var(--mascot-grey) 0%, var(--mascot-grey) 40%, var(--soft-pink) 75%);
  }
  .contact-line {
    position: absolute;
    right: 14px;
    bottom: 26px;
    color: var(--brand-pink);
    font-weight: 500;
    font-size: 17px;
    letter-spacing: 0.3px;
  }
</style>
</head>
<body>
  <main class="letterhead">
    <header class="masthead">
      <div class="brand">
        <span class="brand-dot"></span>
        <span class="brand-name">Tallowmoor</span>
      </div>
    </header>
    <div class="mascot-art" role="img" aria-label="Large grey and pink brand mascot illustration rising from the lower left corner"></div>
    <footer class="contact-line">tallowmoor.co.uk | 0208 555 0173 | sales@tallowmoor.co.uk</footer>
  </main>
</body>
</html>
```